Signage Design job – Healthcare IT Company Needs a Core Values Poster for Office

We want to make a poster for our offices that beautifully presents our core values.

We want the design to be fun, young and colourful while showing some sophistication.

The poster will be visible to the staff (within the open plan office), and the right colours will need to be used to enhance mood and productivity. Perhaps we could be looking at a colour for each core value? Or potentially some other way for each value to stand out? We have other culture posters that have been created in the past that we would like to stay similar to in style for cohesiveness.

Our office walls are primarily white and navy blue with accents of orange, grey, and turquoise.

In terms of size - we aren't 100% on what size we want, but not only will be print it on the walls, we will also be printing out mini versions for people to put in their cubicles so keep that in mind for font legibility.

Fonts can be experimented with, but they main body font should be Source Sans Pro.

It needs to be clear, punchy and stand out from across the office (while being easy on the eye)

We have a series of cartoon guardians that can be incorporated into the design as well.

I have attached a few sample images that can be used as inspiration. We would like more colour throughout the design. 

Final file should be AI or EPS vector file.

Target Market(s)

Internal employees age range from 25-60

Font styles to use
Sans Serif
Other font styles liked:
• Please use Source Sans Pro

Colors
abd037
6b449b
33a6d7
f37122
0355a3
ffcf3e
e34297

Requirements
Must have
• Must use our colors. Must feel fresh and energetic. Must emphasize important key words. Must feel inspirational. Must align with our internal branding. Look at the 4 posters I have included in the files to understand our look. Our company website is www.kelvantis.com
Nice to have
• Mission Statement is not necessary if there isn't enough room on the poster.
Should not have
• Should not be cluttered looking in such a way that you can't get the message.

```html
<!DOCTYPE html>
<html lang="en">
<head>
<meta charset="utf-8">
<title>Kelvantis Core Values Poster</title>
<link rel="stylesheet" href="https://fonts.googleapis.com/css2?family=Source+Sans+3:wght@400;600;700;800&display=swap">
<style>
  :root {
    --backdrop: #c6c6c6;
    --paper: #fdfdfd;
    --body-blue: #1f96d3;
    --navy: #0355a3;
    --deep-navy: #13294b;
    --orange: #f37122;
    --gold: #f7a531;
    --purple: #6b449b;
    --sky: #33a6d7;
    --pale-sky: #d8eaf6;
  }
  * { margin: 0; padding: 0; box-sizing: border-box; }
  html, body {
    width: 1200px; height: 1000px; overflow: hidden;
    background: var(--backdrop);
    font-family: "Source Sans 3", "Source Sans Pro", sans-serif;
  }
  .poster {
    position: absolute; left: 261px; top: 26px;
    width: 630px; height: 882px;
    background: var(--paper);
    transform: scale(1.075); transform-origin: top left;
    box-shadow: 0 6px 18px rgba(0,0,0,.18);
    overflow: hidden;
  }
  .decor { position: absolute; inset: 0; width: 630px; height: 882px; }
  .line {
    position: absolute; height: 22px; line-height: 22px;
    font-size: 15px; font-weight: 600; color: var(--body-blue);
    white-space: nowrap; text-align: justify; text-align-last: justify;
  }
  .line.centered { text-align: center; text-align-last: center; }
  .sm { font-size: 12px; font-weight: 600; }
  .kw {
    display: inline-block; font-size: 21px; font-weight: 800;
    line-height: 21px; padding: 0 3px; letter-spacing: .3px;
  }
  .kw-orange-box { background: var(--gold); color: #fff; }
  .kw-orange-box-navy { background: var(--gold); color: var(--navy); }
  .kw-orange-text { color: var(--orange); padding: 0; }
  .kw-blue-box { background: var(--sky); color: #fff; }
  .kw-navy-box { background: var(--navy); color: #fff; }
  .kw-purple-box { background: var(--purple); color: #fff; }
  .kw-purple-text { color: var(--purple); padding: 0; }
  .kw-navy-text { color: var(--navy); padding: 0; }
  .sign-off {
    position: absolute; left: 436px; top: 742px;
    font-size: 37px; font-weight: 700; color: var(--navy); letter-spacing: -.5px;
  }
  .brand { position: absolute; left: 280px; top: 782px; display: flex; align-items: center; gap: 12px; }
  .brand-mark { width: 64px; height: 64px; background: var(--orange); border-radius: 6px; }
  .brand-name { font-size: 60px; font-weight: 700; color: var(--deep-navy); letter-spacing: -1.5px; line-height: 1; }
</style>
</head>
<body>
<main class="poster">
  <svg class="decor" viewBox="0 0 630 882" aria-hidden="true">
    <polygon points="500,0 615,0 615,118" fill="var(--pale-sky)"/>
    <path d="M13,267 L118,372 Q136,392 118,412 L13,547 Z" fill="var(--pale-sky)"/>
    <polyline points="247,0 305,47" fill="none" stroke="var(--gold)" stroke-width="2"/>
    <polyline points="535,129 570,129 615,84" fill="none" stroke="var(--gold)" stroke-width="2"/>
    <polyline points="13,390 80,459 176,459" fill="none" stroke="var(--navy)" stroke-width="2"/>
    <line x1="13" y1="580" x2="97" y2="580" stroke="var(--gold)" stroke-width="2"/>
    <line x1="570" y1="677" x2="570" y2="777" stroke="var(--navy)" stroke-width="2"/>
  </svg>

  <div class="line" style="top:49px;left:218px;width:255px">We <span class="kw kw-orange-box">PIONEER</span> technologies</div>
  <div class="line" style="top:73px;left:174px;width:342px">and services that are simple, powerful, and</div>
  <div class="line" style="top:95px;left:153px;width:379px">fast, <span class="sm">which help doctors provide excellent patient care on their</span></div>
  <div class="line" style="top:119px;left:143px;width:392px"><span class="sm">own terms.</span> We have an <span class="kw kw-orange-box">ENTREPRENEURIAL</span></div>
  <div class="line" style="top:142px;left:120px;width:415px">spirit. We are <span class="kw kw-orange-text">ADAPTABLE,</span> <span class="kw kw-orange-box-navy">DRIVEN,</span> and</div>
  <div class="line" style="top:168px;left:123px;width:422px">innovative. <span class="sm">Our focus is broad, reaching horizontally through the</span></div>
  <div class="line" style="top:190px;left:120px;width:430px"><span class="sm">healthcare space.</span> We are <span class="kw kw-blue-box">COLLABORATIVE</span> and</div>
  <div class="line" style="top:214px;left:118px;width:434px">communicate openly, honestly, and <span class="kw kw-navy-box">RESPECTFULLY</span></div>
  <div class="line" style="top:238px;left:122px;width:423px"><span class="sm">at all levels.</span> We challenge ourselves to <span class="kw kw-purple-text">EXCELLENCE,</span></div>
  <div class="line" style="top:262px;left:125px;width:420px">we are <span class="kw kw-navy-text">SELFLESS,</span> generous, and contribute at our</div>
  <div class="line" style="top:286px;left:133px;width:425px">highest capacity. <span class="sm">We are members of a team, and we recognize that</span></div>
  <div class="line" style="top:308px;left:142px;width:428px"><span class="sm">our combined efforts make us successful.</span> We welcome challenges</div>
  <div class="line" style="top:332px;left:152px;width:430px">and embrace change. We are <span class="kw kw-orange-text">PASSIONATE</span> about</div>
  <div class="line" style="top:358px;left:173px;width:377px">our vision, <span class="sm">actively expressing our ideas, and making room</span></div>
  <div class="line" style="top:381px;left:183px;width:363px"><span class="sm">for constructive dissent.</span> We are <span class="kw kw-blue-box">SOLUTIONS</span></div>
  <div class="line" style="top:404px;left:185px;width:350px">oriented, take risks, think differently, and pave</div>
  <div class="line" style="top:428px;left:185px;width:353px">our own way as a leader in the market. We are</div>
  <div class="line" style="top:449px;left:175px;width:355px"><span class="kw kw-navy-box">AGILE</span><span class="sm">and “fail fast”.</span> We are<span class="kw kw-purple-box">DISCIPLINED</span></div>
  <div class="line" style="top:474px;left:165px;width:365px">to think carefully, plan well, measure our results,</div>
  <div class="line" style="top:500px;left:145px;width:387px"><span class="sm">and manage the outcomes so that we can succeed in a competitive</span></div>
  <div class="line" style="top:522px;left:118px;width:264px"><span class="sm">environment.</span> We conduct business</div>
  <div class="line" style="top:545px;left:115px;width:261px">with <span class="kw kw-orange-box">INTEGRITY.</span> We are</div>
  <div class="line" style="top:570px;left:97px;width:276px"><span class="kw kw-orange-box">ACCOUNTABLE</span> <span class="sm">to one another,</span></div>
  <div class="line" style="top:594px;left:83px;width:286px">our customers, and our partners. We</div>
  <div class="line" style="top:617px;left:69px;width:297px">strive to maintain affordable prices</div>
  <div class="line" style="top:637px;left:57px;width:307px">by being good stewards of our</div>
  <div class="line" style="top:662px;left:47px;width:317px"><span class="kw kw-orange-box-navy">RESOURCES.</span> We are committed</div>
  <div class="line" style="top:688px;left:40px;width:329px">to having a <span class="kw kw-navy-text">GROWTH</span> mindset and</div>
  <div class="line" style="top:712px;left:70px;width:264px">doing our best today and doing</div>
  <div class="line centered" style="top:735px;left:110px;width:181px">better tomorrow.</div>

  <div class="sign-off">We are</div>
  <div class="brand">
    <span class="brand-mark"></span>
    <span class="brand-name">Kelvantis</span>
  </div>
</main>
</body>
</html>
```